Verdana Back & Limb Business Card

Need a business card using the logo provided. I want brand side of the card to be grey with the logo in the center of the card in white.

On the other side I leave to the designers

Target Market(s)

Personal Injury Attorneys

Industry/Entity Type

Medical

Contact Information for Business Card

Name, CEO. Cell Phone, (Hialeah, Address, Phone) (Homestead, Address, Phone) (Tallahassee, Address, Phone)

Colors

Designer to choose only greyscale colors for use in the design.

Requirements
Must have
• Logo by itself on one side

```html
<!DOCTYPE html>
<html lang="en">
<head>
<meta charset="utf-8">
<title>Verdana Back &amp; Limb – Business Card</title>
<link href="https://fonts.googleapis.com/css2?family=Montserrat:wght@400;500;600&display=swap" rel="stylesheet">
<style>
  :root {
    --backdrop: #adadaa;
    --card: #9bb5bb;
    --card-edge: #4f86c4;
    --ink-light: #ffffff;
    --ink-soft: #f2f6f7;
    --rule: #ffffff;
  }
  * { box-sizing: border-box; margin: 0; padding: 0; }
  html, body {
    width: 1200px; height: 801px; overflow: hidden;
    background: var(--backdrop);
    font-family: "Montserrat", sans-serif;
  }
  .stage {
    width: 1200px; height: 801px;
    display: flex; align-items: center; justify-content: center; gap: 48px;
  }
  .card {
    width: 540px; height: 309px;
    background: var(--card);
    border-radius: 18px;
    border-bottom: 2px solid var(--card-edge);
    box-shadow: 0 14px 30px rgba(0,0,0,0.22);
    position: relative;
    color: var(--ink-light);
  }
  /* Contact side */
  .card--info { display: flex; align-items: center; padding: 0 34px; }
  .info-brand {
    width: 210px;
    font-weight: 600; font-size: 23px; line-height: 1.2; letter-spacing: 1px;
    text-transform: uppercase; color: var(--ink-light);
  }
  .info-rule { width: 1px; height: 190px; background: var(--rule); margin: 0 26px; flex: none; }
  .info-details { font-size: 11.5px; line-height: 1.45; color: var(--ink-soft); white-space: nowrap; }
  .person-name { font-weight: 600; font-size: 17px; letter-spacing: 0.5px; text-transform: uppercase; line-height: 1.2; }
  .person-role { font-size: 12px; margin-bottom: 4px; }
  .contact-line { display: flex; align-items: center; gap: 6px; }
  .contact-line svg { width: 10px; height: 10px; flex: none; }
  .office-phone { font-weight: 500; }
  /* Brand side */
  .card--brand { display: flex; align-items: center; justify-content: center; }
  .brand-name {
    font-weight: 600; font-size: 34px; line-height: 1.2; letter-spacing: 3px;
    text-transform: uppercase; text-align: center; color: var(--ink-light);
  }
</style>
</head>
<body>
<main class="stage">
  <section class="card card--info" aria-label="Contact side">
    <div class="info-brand">Verdana Back &amp; Limb</div>
    <div class="info-rule"></div>
    <div class="info-details">
      <p class="person-name">Daniel Morrow</p>
      <p class="person-role">CEO</p>
      <p class="contact-line">
        <svg viewBox="0 0 10 10"><path d="M2 1 L3.5 1 L4 3 L3 3.8 Q4 6 6.2 7 L7 6 L9 6.5 L9 8 Q8.5 9 7.5 9 Q1 8 1 2 Q1 1 2 1Z" fill="#fff"/></svg>
        555-014-2287
      </p>
      <p class="contact-line">
        <svg viewBox="0 0 10 10"><rect x="0.8" y="2" width="8.4" height="6" fill="none" stroke="#fff" stroke-width="0.9"/><path d="M0.8 2 L5 5.5 L9.2 2" fill="none" stroke="#fff" stroke-width="0.9"/></svg>
        hello@verdanaback.com
      </p>
      <p class="contact-line">
        <svg viewBox="0 0 10 10"><circle cx="5" cy="5" r="4" fill="none" stroke="#fff" stroke-width="0.9"/><ellipse cx="5" cy="5" rx="1.8" ry="4" fill="none" stroke="#fff" stroke-width="0.8"/><path d="M1 5 H9" stroke="#fff" stroke-width="0.8"/></svg>
        verdanabacklimb.com
      </p>
      <p>Cedarholm, Main Office</p>
      <p class="office-phone">P : +1 555 0140-1100</p>
      <p>Ridgemoor, North Office</p>
      <p class="office-phone">P : +1 555 0140-1170</p>
      <p>Lakeshire, Capital Office</p>
      <p class="office-phone">P : +1 555 0140-1370</p>
    </div>
  </section>

  <section class="card card--brand" aria-label="Brand side">
    <p class="brand-name">Verdana<br>Back &amp; Limb</p>
  </section>
</main>
</body>
</html>
```